Job Coaching - Vanta; engaging people to improve their work experience

I need a flyer for Job Coaching. It serves to engage customers (not businesses) with problems in their daily job, typical questions that are handled are:
Do I fit for the job?
Am I using my talents at best in this job?
I have a conflict with my manager/colleagues, what should I do?
My work-life balance is a mess, how can I improve this?
What job fits best with my talents?
I'm getting stressed out from my job, what can I do?
....
This Flyer will be available at GP's, therpeutic practices, pharamcists,...
this flyer should put people in action to contact me
Flyer can be created in English, in the final one the text should be in Dutch; I will make the translation of the selected flyer and provide it at the end

Target Market(s)

consumers / customers / people having a job, but somewhat stuck in it

Industry/Entity Type

Professional Coaching

Requirements
Must have
• the questions mentioned in the project description; mobile number: 0471/389145; email: tom.vermeer@vantacoaching.example; website: www.vantacoaching.example ; it should make also reference to 'Career guidance cheques of the KWOL'

```html
<!DOCTYPE html>
<html lang="en">
<head>
<meta charset="utf-8">
<title>Vanta – TAB Career Guidance Flyer</title>
<link rel="stylesheet" href="https://fonts.googleapis.com/css2?family=Montserrat:wght@300;400;500;600;700&family=Roboto:wght@400;700&display=swap">
<style>
  :root {
    --teal: #33a99a;
    --teal-deep: #2a958a;
    --ocean: #13709a;
    --ink: #1f2024;
    --charcoal-top: #3c3d42;
    --charcoal-bottom: #24252a;
    --mist: #d9dadf;
    --navy: #1d3f74;
    --slate: #5f6066;
    --white: #ffffff;
  }
  * { box-sizing: border-box; margin: 0; padding: 0; }
  html, body { width: 939px; height: 1200px; overflow: hidden; }
  body { background: #ececee; font-family: "Montserrat", sans-serif; }

  .flyer {
    position: absolute; left: 41px; top: 0;
    width: 856px; height: 1200px;
    background: var(--white); overflow: hidden;
  }

  .hero-shapes, .hero-photo { position: absolute; left: 0; top: 0; width: 856px; height: 525px; }

  .brand { position: absolute; left: 30px; top: 48px; display: flex; align-items: center; gap: 14px; }
  .brand-dot { width: 78px; height: 78px; border-radius: 50%; background: var(--teal); }
  .brand-name { font-weight: 500; font-size: 58px; line-height: 1; color: var(--teal); letter-spacing: 1px; }
  .brand-tagline { position: absolute; left: 137px; top: 112px; font-size: 14px; font-weight: 500; color: var(--slate); }

  .website {
    position: absolute; left: 32px; top: 171px; height: 45px;
    display: flex; align-items: center;
    font-size: 13px; color: var(--white); white-space: nowrap;
  }

  .title {
    position: absolute; left: 33px; top: 254px; width: 500px;
    font-family: "Roboto", sans-serif; font-size: 59px; line-height: 63px; color: var(--white);
  }
  .title strong { font-weight: 700; }
  .title span { font-weight: 400; }

  .chat-icon { position: absolute; left: 588px; top: 468px; width: 52px; height: 40px; }
  .contact { position: absolute; left: 652px; top: 468px; color: var(--white); white-space: nowrap; }
  .contact-phone { font-weight: 700; font-size: 25px; line-height: 1; }
  .contact-mail { font-size: 9px; margin-top: 4px; }

  .intro {
    position: absolute; left: 0; top: 525px; width: 856px; height: 196px;
    background: linear-gradient(180deg, var(--charcoal-top), var(--charcoal-bottom));
    padding: 20px 40px 0 42px; color: var(--white);
    font-size: 13.6px; font-weight: 300; line-height: 16.6px;
  }
  .intro p + p { margin-top: 15px; }

  .story {
    position: absolute; left: 0; top: 721px; width: 392px; height: 197px;
    padding: 32px 30px 0 42px;
    font-size: 16px; line-height: 21px; text-align: justify; color: var(--ink);
  }
  .counseling {
    position: absolute; left: 0; top: 918px; width: 392px; height: 210px;
    background: var(--mist); padding: 36px 26px 0 42px; color: var(--ink);
    font-size: 18.5px; font-weight: 600; line-height: 22px;
  }
  .counseling p + p { margin-top: 28px; }

  .questions {
    position: absolute; left: 392px; top: 721px; width: 464px; height: 407px;
    background: var(--teal); padding: 14px 58px 0 36px; color: var(--white);
  }
  .questions h2 { font-size: 18.5px; font-weight: 600; line-height: 21.5px; }
  .question-list { list-style: none; margin-top: 15px; }
  .question-list li {
    position: relative; padding-left: 24px; font-size: 16px; line-height: 21px; margin-bottom: 18px;
  }
  .question-list li::before {
    content: ""; position: absolute; left: 0; top: 5px;
    width: 12px; height: 12px; border-radius: 50%; background: var(--white);
  }
  .questions .cta { font-size: 18.5px; font-weight: 700; margin-top: 4px; }

  .footer {
    position: absolute; left: 0; top: 1128px; width: 856px; height: 72px;
    display: flex; align-items: center; justify-content: center; gap: 14px;
    color: var(--navy);
  }
  .partner-name { font-size: 24px; font-weight: 700; letter-spacing: -0.5px; }
  .partner-note { font-size: 17px; font-weight: 400; }
</style>
</head>
<body>
<main class="flyer">

  <svg class="hero-photo" viewBox="0 0 856 525" role="img" aria-label="Photo of the career coach in a red shirt standing in front of a desk with a laptop">
    <defs>
      <linearGradient id="photoTone" x1="0" y1="0" x2="1" y2="1">
        <stop offset="0" stop-color="#4d4e55"/>
        <stop offset="0.5" stop-color="#7a3a47"/>
        <stop offset="1" stop-color="#a2404f"/>
      </linearGradient>
    </defs>
    <polygon points="392,0 856,0 856,525 532,525 362,216 266,216" fill="url(#photoTone)"/>
  </svg>

  <svg class="hero-shapes" viewBox="0 0 856 525" aria-hidden="true">
    <defs>
      <linearGradient id="heroTeal" x1="0" y1="0" x2="1" y2="1">
        <stop offset="0" stop-color="#2f9f94"/>
        <stop offset="1" stop-color="#36ad9d"/>
      </linearGradient>
      <linearGradient id="bandTeal" x1="0" y1="0" x2="1" y2="0">
        <stop offset="0" stop-color="#33a99a"/>
        <stop offset="0.7" stop-color="#2d9c93"/>
        <stop offset="1" stop-color="#1d7f98"/>
      </linearGradient>
      <linearGradient id="contactBand" x1="0" y1="0" x2="1" y2="0">
        <stop offset="0" stop-color="#33a99a"/>
        <stop offset="1" stop-color="#13709a"/>
      </linearGradient>
    </defs>
    <polygon points="0,216 362,216 532,525 0,525" fill="url(#heroTeal)"/>
    <polygon points="0,171 243,171 266,216 0,216" fill="url(#bandTeal)"/>
    <polygon points="565,449 856,449 856,525 525,525" fill="url(#contactBand)"/>
  </svg>

  <div class="brand">
    <span class="brand-dot"></span>
    <span class="brand-name">VANTA</span>
  </div>
  <p class="brand-tagline">professional coaching</p>

  <p class="website">www.vantacoaching.example</p>

  <h1 class="title"><strong>TAB - Career Guidance</strong><br><span>(with Career Vouchers)</span></h1>

  <svg class="chat-icon" viewBox="0 0 54 42" aria-hidden="true">
    <path d="M4 4h28a3 3 0 0 1 3 3v14a3 3 0 0 1-3 3H14l-8 7v-7H4a3 3 0 0 1-3-3V7a3 3 0 0 1 3-3z" fill="none" stroke="#fff" stroke-width="2.4"/>
    <circle cx="12" cy="14" r="2" fill="#fff"/><circle cx="18" cy="14" r="2" fill="#fff"/><circle cx="24" cy="14" r="2" fill="#fff"/>
    <path d="M24 18h25a3 3 0 0 1 3 3v11a3 3 0 0 1-3 3h-2v6l-7-6H24a3 3 0 0 1-3-3V21a3 3 0 0 1 3-3z" fill="#fff"/>
    <circle cx="30" cy="27" r="2" fill="#1d7f98"/><circle cx="37" cy="27" r="2" fill="#1d7f98"/><circle cx="44" cy="27" r="2" fill="#1d7f98"/>
  </svg>
  <div class="contact">
    <p class="contact-phone">0471/389145</p>
    <p class="contact-mail">tom.vermeer@vantacoaching.example</p>
  </div>

  <section class="intro">
    <p>We easily spend 8 hours a day on our professional pursuits, our job. If we assume that we sleep about 8 hours a day, that's 50% of our active time. We actually spend more time with our colleagues than with our partner and/or children.</p>
    <p>In addition, if things are not going well during those 8 hours, it also impacts the other 8 waking hours. If we don't feel good about ourselves at work, our family members, friends and acquaintances feel it too.</p>
    <p>So we'd better make sure that we spend those 8 hours meaningfully and, at best, get energy from it too. That we can accomplish a piece of our personal accomplishments there.</p>
  </section>

  <section class="story">
    <p>Unfortunately, not every career goes smoothly, and it is even very normal that there are ups and downs this, nowadays more than 40-year career. But we can strive to keep these downs as short as possible and the ups as long as possible.</p>
  </section>

  <section class="counseling">
    <p>And that's where Career Counseling comes into play.</p>
    <p>During this career counseling, we take a close look at your personal situation.</p>
  </section>

  <section class="questions">
    <h2>Do you recognize yourself in any of the following questions?</h2>
    <ul class="question-list">
      <li>How can I get more energy from my job?</li>
      <li>How can I get a better work-life balance?</li>
      <li>What are my talents?</li>
      <li>How can I work better with my manager and/or colleagues?</li>
      <li>Do you know what you want, but do not dare to take the step?</li>
      <li>Or maybe you think you have more up your sleeve than you do today?</li>
    </ul>
    <p class="cta">Then we will work on this together</p>
  </section>

  <footer class="footer">
    <span class="partner-name">KWOL</span>
    <span class="partner-note">Career cheques can be used</span>
  </footer>

</main>
</body>
</html>
```